Visually Compelling Flyer Design - Orvane Benefits

We are a life insurance company looking to create visually compelling flyers that gain attention of potential buyers and simplify the concept. It should be professional, friendly, approachable in nature. Our logo and several rough drafts are included.
We are looking to refine this look and make it ultra professional, clean and easy to follow. A creative brief with brand guidelines is also included.
FLYER 1 — PAY YOURSELF FIRST
EYEBROW TAG
YOUR COMPANY JUST UPGRADED YOUR BENEFITS
HEADLINE
One small decision. A lifetime of protection.
SUBHEADLINE
Permanent life insurance + long-term care coverage, starting at $1 a day.
EYEBROW TAG
CHOOSE YOUR DAILY INVESTMENT
STAT — TIER 1
$1 / day → $20,000 Life Insurance
STAT — TIER 2 (HERO — make this one biggest/most prominent)
$2 / day → $40,000 Life Insurance
★ Most Popular
STAT — TIER 3
$3 / day → $60,000 Life Insurance
CAPTION
Rate locked at enrollment. Benefit never decreases.
EYEBROW TAG
THREE BENEFITS. ONE POLICY.
SUBHEADLINE
Your money works three ways.
CALLOUT — BENEFIT 1
01 | Cash Value Growth
BODY
Averages 6% annually over the last 50 years — guaranteed never to fall below 3%. Better than any savings account. And if you ever need it, you can borrow against it. It's your money.
CALLOUT — BENEFIT 2
02 | Tax-Free Death Benefit
BODY
From day one, your family is protected. The full benefit is paid tax-free to the person you choose — no waiting period, no exceptions. That's your legacy, preserved.
CALLOUT — BENEFIT 3
03 | Long-Term Care Coverage
BODY
70% of Americans will need long-term care. This plan pays 75% of your benefit — upfront and tax-free — to cover those costs while you're still alive. Your retirement savings stay intact. Your family stays protected.
EYEBROW TAG
ALREADY HAVE LIFE INSURANCE THROUGH WORK?
SUBHEADLINE
That's term. It ends when you need it most.
BODY
Term life insurance is designed for temporary needs — protecting your paycheck, your mortgage, your kids while they're home. When you retire, the house is paid off and your children are grown. Term ends because the need ends.
BODY
But one need never ends: your final expenses and the cost of long-term care. This permanent plan stays with you after retirement — when term coverage is gone and getting new coverage is expensive or impossible.
COMPARISON — LEFT COLUMN HEADER
✕ TERM LIFE
COMPARISON — LEFT COLUMN ITEMS
Gets more expensive with age
Ends at retirement
No cash value
Temporary protection only
COMPARISON — RIGHT COLUMN HEADER
✓ THIS PLAN
COMPARISON — RIGHT COLUMN ITEMS
Rate locked forever at enrollment
Stays with you after retirement
Builds real cash value
Permanent protection for life
EYEBROW TAG
WHAT MAKES THIS DIFFERENT
SUBHEADLINE
Built for you. Stays with you.
CALLOUT
✓ Guaranteed Issued
No medical exams. No questions asked. You qualify.
CALLOUT
✓ Group Rate
Because you work here, you get pricing individuals can't access on their own.
CALLOUT
✓ Rate Locked Forever
Your premium never increases. Your benefit never decreases.
CALLOUT
✓ Portable
Change jobs. Retire. Your policy comes with you at the same rate.
CALLOUT
✓ Family Coverage
Protect your spouse and children under the same plan.
SUBHEADLINE
Protect retirement. Preserve dignity. Plan ahead.
CTA
Be on the lookout for your personalized coverage details.
CAPTION
Brokered by Orvane Benefits · Underwritten by TrelloraLife
FLYER 2 — THE LONG-TERM CARE REALITY
EYEBROW TAG
WHAT MOST PEOPLE DON'T KNOW — BUT SHOULD
HEADLINE
Most Americans are unprepared. You don't have to be.
SUBHEADLINE
The long-term care gap is real — and it affects families like yours.
EYEBROW TAG
THE NUMBERS ARE HARD TO IGNORE
STAT
70%
of Americans age 65 and older will need some form of long-term care during their lifetime.
CAPTION
Source: Pike & Marsden, Review of Elder Welfare and Civic Planning, 2018
STAT
3–4%
of Americans over 50 own a private long-term care insurance policy. The gap between who needs it and who has it is staggering.
CAPTION
Source: Dunn & Solberg, QRT Wellness Wire, 2023
STAT
$700 Billion+
Estimated annual U.S. long-term care cost — and it's growing every year.
CAPTION
Source: Brandt Lowe & Petrasek, Civic Policy Roundtable, 2020
STAT
$470 Billion
The estimated value of unpaid care provided by family members every year. That's the real cost — measured in time, stress, and financial sacrifice.
CAPTION
Source: Lindqvist & Oram, Harborline Institute
STAT
80%
of total long-term care spending goes directly to assist retirees. This isn't a young person's problem. But the time to plan is now.
CAPTION
SUBHEADLINE
Long-term care doesn't just cost money. It costs families.
BODY
When there's no plan in place, the people you love absorb the impact — financially, emotionally, and physically. Retirement savings built over a lifetime can disappear in months. Family members step back from their own lives to provide care. Dignity becomes a daily negotiation.
BODY
This is not inevitable. A small decision today changes the entire outcome.
EYEBROW TAG
THE SOLUTION
HEADLINE
The Pay Yourself First Principle.
BODY
Take the first $1, $2, or $3 you make every day and invest it in a permanent life insurance policy that includes long-term care coverage — underwritten by TrelloraLife, offered through your employer at a group rate, and Guaranteed Issued for everyone.
STAT
$1 / day → $20,000 $2 / day → $40,000 $3 / day → $60,000
BODY
The benefit includes three protections in one: a cash value that grows at an average of 6% annually, a tax-free death benefit for your family, and long-term care coverage that pays 75% of your benefit upfront — tax-free — when you need care most.
SUBHEADLINE
Whether you're single, married, with children or without — there is protection in this plan for you.
HEADLINE
CTA
Look for your personalized offer. Coverage details are coming your way.
CAPTION
COPY RULES FOR DESIGNERS
Headlines are one idea only. Never more than two lines.
Stats stand alone. Never buried in a paragraph.
Body copy maxes at 3 sentences per block. If it's longer, cut it.
The $2/day tier is always the hero. Always.
"Guaranteed Issued" appears on both flyers. It's the most important trust signal.
TrelloraLife is always attributed. Always.
The tagline is: Protect retirement. Preserve dignity. Plan ahead. — Use it verbatim.
Target Market(s)
Average Americans with a family - adults looking for life insurance
Industry/Entity Type
Life Insurance & Financial Retirement

```html
<!DOCTYPE html>
<html lang="en">
<head>
<meta charset="utf-8">
<title>Orvane Benefits — The Long-Term Care Reality</title>
<link rel="stylesheet" href="https://fonts.googleapis.com/css2?family=Fira+Sans:wght@500;600;700;800&family=Open+Sans:wght@400;600;700&display=swap">
<style>
  :root{
    --navy:#1b3c6d;
    --navy-deep:#17335f;
    --blue:#1f5fa8;
    --blue-bright:#2a6cbc;
    --cyan:#2bb5d4;
    --ink:#1d3a6b;
    --grey:#7d7f86;
    --panel:#eef0f6;
    --white:#ffffff;
    --stage:#d6d8e1;
    --head:"Fira Sans", sans-serif;
    --body:"Open Sans", sans-serif;
  }
  *{box-sizing:border-box;margin:0;padding:0}
  html,body{width:1200px;height:900px;overflow:hidden;background:var(--stage)}
  .flyer{position:absolute;left:260px;top:10px;width:680px;height:880px;background:var(--white);overflow:hidden;box-shadow:0 6px 18px rgba(20,30,60,.18);font-family:var(--body)}
  .abs{position:absolute}

  /* header */
  .hero{left:0;top:0;width:680px;height:232px;background:linear-gradient(90deg,#1a4686 0%,#1f56a0 55%,#2468b6 100%)}
  .hero-photo{left:395px;top:14px;width:285px;height:218px;background:linear-gradient(160deg,#5f7fae 0%,#9aa9c2 40%,#6e5a4c 78%,#2a5fa6 100%);opacity:.85}
  .brand{left:22px;top:22px;display:flex;align-items:center;gap:10px}
  .brand-dot{width:62px;height:62px;border-radius:50%;background:var(--white)}
  .brand-name{font-family:var(--head);font-weight:600;color:var(--white);line-height:1}
  .brand-name span{display:block;font-size:27px;letter-spacing:.5px}
  .brand-name span+span{font-size:20px;letter-spacing:1px;margin-top:3px}
  .eyebrow{left:20px;top:101px;font-family:var(--body);font-weight:600;font-size:11.5px;color:var(--white)}
  .headline{left:22px;top:113px;font-family:var(--head);font-weight:700;font-size:33px;line-height:31px;color:var(--cyan);letter-spacing:.2px}
  .subhead{left:22px;top:216px;font-weight:700;font-size:12px;color:var(--white)}

  /* numbers */
  .numbers{left:0;top:232px;width:440px;height:286px;background:var(--white)}
  .numbers-title{left:0;top:10px;width:440px;text-align:center;font-family:var(--head);font-weight:700;font-size:15px;color:var(--navy)}
  .divider{left:212px;top:35px;width:2px;height:210px;background:var(--cyan)}
  .stat-big{font-family:var(--head);font-weight:700;color:var(--ink);font-size:68px;line-height:1;letter-spacing:-1px}
  .stat-big small{font-size:44px;letter-spacing:0}
  .stat-70{left:40px;top:42px}
  .stat-34{left:250px;top:42px}
  .people{left:30px;top:116px;width:154px;height:46px;border-radius:4px;background:linear-gradient(90deg,var(--navy) 0%,var(--blue) 45%,var(--cyan) 100%)}
  .vs{left:195px;top:124px;width:36px;height:36px;border-radius:50%;background:var(--navy);color:var(--white);font-family:var(--head);font-weight:700;font-size:13px;display:flex;align-items:center;justify-content:center}
  .donut{left:290px;top:104px}
  .caption{font-weight:600;font-size:12px;line-height:16px;color:var(--grey);text-align:center}
  .caption-70{left:12px;top:178px;width:186px}
  .caption-34{left:224px;top:180px;width:212px}
  .source{left:0;top:261px;width:440px;text-align:center;font-size:9px;font-weight:600;color:var(--grey)}

  /* figures column */
  .figures{left:440px;top:232px;width:240px;height:286px;background:var(--panel);text-align:center;padding:6px 10px 0}
  .figure-num{font-family:var(--head);font-weight:700;color:var(--ink);font-size:28px;line-height:28px}
  .figure-num small{font-size:12px;margin-left:4px}
  .figure-text{font-size:10px;line-height:11px;color:#6f7178;margin-top:1px}
  .figure-source{font-size:9px;font-weight:700;color:var(--blue);line-height:11px;margin:4px 0 5px}

  /* solution */
  .solution{left:0;top:518px;width:440px;height:266px;background:var(--panel);text-align:center}
  .solution-title{left:0;top:4px;width:440px;font-family:var(--head);font-weight:700;font-size:25px;color:var(--navy)}
  .solution-sub{left:0;top:33px;width:440px;font-family:var(--head);font-weight:700;font-size:16px;color:var(--navy)}
  .solution-body{left:8px;top:52px;width:424px;font-size:9.6px;line-height:11.4px;color:var(--blue)}
  .tier{top:98px;width:100px;text-align:center;color:var(--navy)}
  .tier b{font-family:var(--head);font-weight:700;font-size:27px;line-height:28px}
  .tier i{font-style:normal;font-size:11px}
  .tier span{display:block;font-size:11px;line-height:12px}
  .tier-1{left:38px}
  .tier-2{left:180px;top:99px;width:93px;height:47px;border-radius:9px;background:var(--cyan);padding-top:2px}
  .tier-3{left:306px}
  .includes{left:0;top:151px;width:440px;font-size:12px;color:var(--navy)}
  .protect{top:172px;text-align:center;color:var(--blue);font-size:11.5px;line-height:13px}
  .protect h4{font-family:var(--head);font-weight:700;font-size:16px;line-height:18px;color:var(--navy)}
  .protect strong{font-family:var(--head);font-weight:700;font-size:24px;color:var(--navy)}
  .protect-1{left:38px;width:120px}
  .protect-2{left:169px;width:120px}
  .protect-3{left:288px;width:140px}
  .upfront{left:0;top:248px;width:440px;font-size:12px;color:var(--navy)}

  /* cost panel */
  .cost{left:440px;top:518px;width:240px;height:266px;background:var(--navy);padding:10px 12px 0}
  .cost h3{font-family:var(--head);font-weight:700;font-size:26px;line-height:23px;color:var(--white)}
  .cost p{font-size:11px;line-height:12.3px;color:var(--cyan);margin-top:9px}
  .cost p+p{margin-top:8px}

  /* footer */
  .footer{left:0;top:784px;width:440px;height:96px;background:var(--navy);padding:14px 0 0 22px;color:var(--white)}
  .footer p{font-size:12px;line-height:14.5px}
  .tagline{display:flex;align-items:center;gap:4px;margin:8px 0 0 -5px;font-family:var(--head);font-weight:700;font-size:15.5px}
  .tagline i{width:14px;height:14px;border-radius:50%;background:var(--cyan);display:inline-block;margin-left:3px}
  .brokered{font-weight:700;font-size:10.5px;margin:9px 0 0 50px}
  .cta{left:440px;top:784px;width:240px;height:96px;background:var(--white);text-align:center;padding-top:10px}
  .cta p{font-weight:700;font-size:10px;line-height:11.5px;color:#111}
  .cta-brand{display:flex;align-items:center;justify-content:center;gap:8px;margin-top:12px}
  .cta-brand .brand-dot{width:36px;height:36px;background:var(--blue)}
  .cta-brand .brand-name{color:var(--blue)}
  .cta-brand .brand-name span{font-size:18px}
  .cta-brand .brand-name span+span{font-size:13px;margin-top:1px}
</style>
</head>
<body>
<main class="flyer">
  <section class="abs hero">
    <div class="abs hero-photo" role="img" aria-label="Photo of an older couple seen from behind, sitting close together on a wooden bench"></div>
    <div class="abs brand">
      <div class="brand-dot"></div>
      <div class="brand-name"><span>ORVANE</span><span>BENEFITS</span></div>
    </div>
    <p class="abs eyebrow">WHAT MOST PEOPLE DON'T KNOW — BUT SHOULD</p>
    <h1 class="abs headline">Most Americans are<br>unprepared.<br>You don't have to be.</h1>
    <p class="abs subhead">The long-term care gap is real — and it affects families like yours.</p>
  </section>

  <section class="abs numbers">
    <h2 class="abs numbers-title">THE NUMBERS ARE HARD TO IGNORE</h2>
    <div class="abs divider"></div>
    <div class="abs stat-big stat-70">70<small>%</small></div>
    <div class="abs people" role="img" aria-label="Row of seven person pictograms shaded from navy to cyan"></div>
    <div class="abs vs">VS</div>
    <p class="abs caption caption-70">of Americans age 65 and older will need some form of long-term care during their lifetime.</p>
    <div class="abs stat-big stat-34">3-4<small>%</small></div>
    <svg class="abs donut" width="76" height="76" viewBox="0 0 76 76" aria-hidden="true">
      <circle cx="38" cy="38" r="31" fill="none" stroke="var(--cyan)" stroke-width="9" stroke-dasharray="180 15" transform="rotate(-80 38 38)"/>
      <text x="38" y="44" text-anchor="middle" font-family="Fira Sans, sans-serif" font-weight="700" font-size="17" fill="#1d3a6b">3-4<tspan font-size="11">%</tspan></text>
    </svg>
    <p class="abs caption caption-34">of Americans over 50 own a private long-term care insurance policy. The gap between who needs it and who has it is staggering.</p>
    <p class="abs source">Source: Pike &amp; Marsden, Review of Elder Welfare and Civic Planning, 2018</p>
  </section>

  <aside class="abs figures">
    <div class="figure-num">$700<small>Billion+</small></div>
    <p class="figure-text">Estimated annual U.S. long-term care cost — and it's growing every year.</p>
    <p class="figure-source">Source: Brandt Lowe &amp; Petrasek,<br>Civic Policy Roundtable, 2020</p>
    <div class="figure-num">$470<small>Billion</small></div>
    <p class="figure-text">The estimated value of unpaid care provided by family members every year. That's the real cost — measured in time, stress, and financial sacrifice.</p>
    <p class="figure-source">Source: Lindqvist &amp; Oram, Harborline Institute</p>
    <div class="figure-num">80%</div>
    <p class="figure-text">of total long-term care spending goes directly to assist retirees. This isn't a young person's problem. But the time to plan is now.</p>
    <p class="figure-source">Source: Lindqvist &amp; Oram, Harborline Institute</p>
  </aside>

  <section class="abs solution">
    <h2 class="abs solution-title">THE SOLUTION</h2>
    <h3 class="abs solution-sub">The Pay Yourself First Principle.</h3>
    <p class="abs solution-body">Take the first $1, $2, or $3 you make every day and invest it in a permanent life insurance policy that includes long-term care coverage — underwritten by TrelloraLife, offered through your employer at a group rate, and Guaranteed Issued for everyone.</p>
    <div class="abs tier tier-1"><b>$1</b> <i>/ day</i><span>$20,000</span></div>
    <div class="abs tier tier-2"><b>$2</b> <i>/ day</i><span>$40,000</span></div>
    <div class="abs tier tier-3"><b>$3</b> <i>/ day</i><span>$60,000</span></div>
    <p class="abs includes">The benefit includes three protections</p>
    <div class="abs protect protect-1"><h4>Cash Value</h4>that grows at an<br>average<br><strong>6%</strong> annually,</div>
    <div class="abs protect protect-2"><h4>Tax-Free<br>Death</h4>benefit for<br>your family,</div>
    <div class="abs protect protect-3"><h4>Long-Term</h4>care coverage that<br>pays <strong>75%</strong> of<br>your benefit</div>
    <p class="abs upfront">upfront — tax-free — when you need care most.</p>
  </section>

  <section class="abs cost">
    <h3>Long-term care doesn't just cost money. It costs families.</h3>
    <p>When there's no plan in place, the people you love absorb the impact — financially, emotionally, and physically. Retirement savings built over a lifetime can disappear in months. Family members step back from their own lives to provide care. Dignity becomes a daily negotiation.</p>
    <p>This is not inevitable.</p>
    <p>A small decision today changes the entire outcome.</p>
  </section>

  <footer class="abs footer">
    <p>Whether you're single, married, with children or without<br>— there is protection in this plan for you.</p>
    <div class="tagline"><i></i>Protect retirement.<i></i>Preserve dignity.<i></i>Plan ahead.</div>
    <p class="brokered">Brokered by Orvane Benefits · Underwritten by TrelloraLife</p>
  </footer>

  <div class="abs cta">
    <p>Look for your personalized offer. Cover-age<br>details are coming your way.</p>
    <div class="cta-brand">
      <div class="brand-dot"></div>
      <div class="brand-name"><span>ORVANE</span><span>BENEFITS</span></div>
    </div>
  </div>
</main>
</body>
</html>
```